Refresh Application User Interface

Brindlecove wishes to update the look of its business applications. Two representative forms are shown below. Please note, we are not considering changes in functionality or usability. Our goal is a cleaner, more contemporary design.

Industry/Entity Type

Business

```html
<!DOCTYPE html>
<html lang="en">
<head>
<meta charset="utf-8">
<title>Brindlecove – Purchase Order</title>
<link rel="stylesheet" href="https://fonts.googleapis.com/css2?family=Open+Sans:wght@400;600;700&display=swap">
<style>
:root{
  --bar:#2f3238;
  --ink:#2b2f36;
  --muted:#8a94a6;
  --blue:#3b82d6;
  --green:#4cb84c;
  --red:#e5455f;
  --line:#d9dde3;
  --soft:#f4f5f7;
  --side:#eceef2;
  --side-active:#f6f7f9;
}
*{box-sizing:border-box;margin:0;padding:0}
html,body{width:1200px;height:861px;overflow:hidden;background:#fff;font-family:"Open Sans",sans-serif;color:var(--ink)}
.canvas{position:relative;width:1200px;height:861px}
.abs{position:absolute}
.topbar{left:0;top:0;width:1200px;height:54px;background:var(--bar);color:#fff;font-size:17px}
.topbar .t{position:absolute;top:13px;white-space:nowrap}
.topbar b{font-weight:600}
.topbar .logout{color:var(--red)}
.nav{position:absolute;top:78px;font-size:24px;color:#4a4f57;white-space:nowrap}
.nav.sep{color:#9aa0a8}
.nav.on{color:var(--blue);font-weight:600}
.brand{position:absolute;top:78px;left:998px;font-size:25px;font-weight:700;color:var(--blue)}
.subnav{position:absolute;top:135px;font-size:21px;color:#9aa6b8;white-space:nowrap}
.subnav.on{color:var(--ink)}
.underline{height:4px;background:var(--blue);top:173px}
.rule{left:0;top:179px;width:1048px;height:1px;background:var(--line)}
.menu{left:742px;top:180px;width:149px;background:var(--side-active);font-size:13px;color:#7d8898}
.menu div{padding:6px 10px}
.side{left:1048px;width:152px;display:flex;align-items:center;justify-content:center;font-size:22px;color:#97a0ad}
.title{left:26px;top:197px;font-size:24px}
.label{font-size:14px}
.field{position:absolute;height:26px;border:1px solid var(--line);background:#fff;border-radius:2px;font-size:12px;padding:0 10px;line-height:24px;white-space:nowrap;overflow:hidden}
.sel::after{content:"";position:absolute;right:7px;top:10px;border:4px solid transparent;border-top:5px solid #666}
.check{position:absolute;width:20px;height:20px;border:1px solid #c5cad2;border-radius:4px;background:#fff}
.link{color:var(--blue);text-decoration:underline}
.toolbar{left:0;top:331px;width:1048px;height:36px;background:var(--soft)}
.hdr{top:374px;font-size:14px;color:#4a4f57}
.band{left:0;width:1048px;background:var(--soft)}
.txt{font-size:14px;white-space:nowrap}
.bottombar{left:0;top:795px;width:1200px;height:66px;border-top:1px solid var(--line);background:#fff}
.bottombar .t{position:absolute;font-size:17px;color:var(--blue);top:20px;white-space:nowrap}
.hint{left:651px;top:10px;width:240px;text-align:center;font-size:16px;color:var(--muted);line-height:23px;white-space:nowrap}
svg{position:absolute}
</style>
</head>
<body>
<div class="canvas">

<div class="abs topbar">
  <span class="t" style="left:15px">Logged In As <b>Dana Pratt</b></span>
  <svg style="left:213px;top:19px" width="16" height="16" viewBox="0 0 16 16"><circle cx="8" cy="8" r="6" fill="#fff"/><circle cx="8" cy="8" r="2.5" fill="#2f3238"/></svg>
  <span class="t" style="left:249px">Current Role <b>administrator</b></span>
  <svg style="left:473px;top:20px" width="13" height="13" viewBox="0 0 13 13"><circle cx="6.5" cy="6.5" r="6.5" fill="#fff"/><path d="M3.5 5l3 3 3-3" fill="#2f3238"/></svg>
  <svg style="left:635px;top:12px" width="24" height="30" viewBox="0 0 24 30" fill="none" stroke="#fff" stroke-width="1.6"><path d="M8 17V4a2 2 0 014 0v9l7 2v8l-3 5H9l-5-8 2-2 2 3"/></svg>
  <span class="t" style="left:669px">Touch</span>
  <svg style="left:739px;top:13px" width="34" height="28" viewBox="0 0 34 28" fill="none" stroke="#fff" stroke-width="1.6"><rect x="1" y="1" width="26" height="18"/><path d="M5 5h18"/><circle cx="27" cy="21" r="5" fill="#4cb84c" stroke="none"/></svg>
  <span class="t" style="left:781px">New Tab</span>
  <svg style="left:867px;top:12px" width="30" height="30" viewBox="0 0 30 30" fill="none" stroke="#fff" stroke-width="1.5"><circle cx="15" cy="15" r="13"/><path d="M11 12a4 4 0 118 0c0 3-4 3-4 6"/><circle cx="15" cy="22" r="1" fill="#fff"/></svg>
  <span class="t" style="left:902px">Help</span>
  <svg style="left:962px;top:12px" width="30" height="30" viewBox="0 0 30 30" fill="none" stroke="#fff" stroke-width="1.6"><path d="M6 16a9 9 0 0118 0M5 15h4v7H5zM21 15h4v7h-4zM23 22c0 4-4 5-8 5"/></svg>
  <span class="t" style="left:994px">Support</span>
  <svg style="left:1080px;top:12px" width="30" height="30" viewBox="0 0 30 30" fill="none" stroke="#e5455f" stroke-width="1.6"><path d="M18 3H3v24h15M10 15h17M22 10l5 5-5 5"/></svg>
  <span class="t logout" style="left:1119px">Log Out</span>
</div>

<span class="nav" style="left:27px">Home</span>
<span class="nav sep" style="left:118px">|</span>
<span class="nav" style="left:150px">eSource</span>
<span class="nav sep" style="left:264px">|</span>
<span class="nav on" style="left:296px">eBuy</span>
<span class="nav sep" style="left:377px">|</span>
<span class="nav" style="left:408px">eRequest</span>
<span class="nav sep" style="left:536px">|</span>
<span class="nav" style="left:568px">eStock</span>
<span class="nav sep" style="left:666px">|</span>
<span class="nav" style="left:699px">ePlan</span>
<span class="nav sep" style="left:784px">|</span>
<span class="nav" style="left:815px">Preferences</span>
<div class="brand">Brindlecove</div>

<div class="subnav on" style="left:27px">Orders</div>
<div class="abs underline" style="left:27px;width:63px"></div>
<div class="subnav" style="left:118px">Receipts</div>
<div class="subnav" style="left:226px">Shipments</div>
<div class="subnav" style="left:355px">Invoices</div>
<div class="subnav" style="left:459px">Pricing</div>
<div class="subnav" style="left:555px">Tables</div>
<div class="subnav" style="left:641px">Reports</div>
<div class="subnav on" style="left:742px">Inquiries</div>
<div class="abs underline" style="left:742px;width:83px"></div>
<div class="subnav" style="left:853px">Periodic Tasks</div>
<div class="subnav" style="left:1014px">Workflows</div>
<div class="abs rule"></div>

<div class="abs side" style="top:180px;height:150px;background:var(--side)">Header</div>
<div class="abs side" style="top:330px;height:163px;background:var(--side-active)">Lines</div>
<div class="abs side" style="top:493px;height:146px;background:var(--side)">Changes</div>
<div class="abs side" style="top:639px;height:156px;background:var(--side);color:var(--green)">
  <svg style="position:static;margin-right:10px" width="26" height="26" viewBox="0 0 26 26"><circle cx="13" cy="13" r="13" fill="#4cb84c"/><path d="M7 13l4 4 8-8" stroke="#fff" stroke-width="2.5" fill="none"/></svg>Notes</div>

<div class="abs title">Purchase Order</div>
<div class="abs label" style="left:35px;top:247px">Order #</div>
<div class="abs" style="left:111px;top:249px;font-size:12px">100159</div>
<div class="abs" style="left:226px;top:247px;font-size:13px;color:var(--green)">Regular Purchase Order</div>
<div class="field" style="left:215px;top:277px;width:281px;height:27px;font-size:12px">Harborline Medical Supply, Easton MA</div>
<div class="abs" style="left:888px;top:247px;font-size:13px;color:var(--blue)">mpletion</div>

<div class="abs menu">
  <div>Inventory Details</div>
  <div style="padding-top:2px;border-bottom:3px solid #fff">Stock Status</div>
  <div style="padding-top:8px">Product Sourcing</div>
</div>

<div class="abs toolbar">
  <svg style="left:20px;top:7px" width="20" height="22" viewBox="0 0 20 22"><path d="M17 2H3l8 9-8 9h14" fill="none" stroke="#3b82d6" stroke-width="3"/></svg>
  <svg style="left:52px;top:6px" width="22" height="24" viewBox="0 0 22 24" fill="none" stroke="#3b82d6" stroke-width="1.3"><rect x="1" y="1" width="13" height="17"/><rect x="7" y="5" width="13" height="17" fill="#fff"/><path d="M10 10h7M10 13h7M10 16h7"/></svg>
  <svg style="left:84px;top:6px" width="22" height="24" viewBox="0 0 22 24" fill="none" stroke="#3b82d6" stroke-width="1.3"><rect x="2" y="3" width="14" height="18"/><rect x="6" y="1" width="6" height="4"/><rect x="8" y="8" width="12" height="15" fill="#fff"/><path d="M11 12h6M11 15h6M11 18h6"/></svg>
  <svg style="left:118px;top:7px" width="22" height="22" viewBox="0 0 22 22" fill="none" stroke="#3b82d6" stroke-width="2"><path d="M5 2v17M1 15l4 5 4-5M12 4h9M12 9h7M12 14h5M12 19h3"/></svg>
  <svg style="left:152px;top:8px" width="18" height="18" viewBox="0 0 18 18" stroke="#e5455f" stroke-width="3"><path d="M2 2l14 14M16 2L2 16"/></svg>
  <svg style="left:816px;top:8px" width="46" height="20" viewBox="0 0 46 20" fill="none" stroke="#7d8898" stroke-width="1.3"><path d="M2 2v16M14 2L4 10l10 8zM26 2l-10 8 10 8z"/></svg>
  <div class="abs" style="left:886px;top:9px;font-size:13px">Page 1 of 1</div>
  <svg style="left:976px;top:8px" width="46" height="20" viewBox="0 0 46 20" fill="none" stroke="#7d8898" stroke-width="1.3"><path d="M2 2l10 8-10 8zM12 2l10 8-10 8zM32 2l10 8-10 8zM44 2v16"/></svg>
</div>

<div class="abs hdr" style="left:31px">Line #</div>
<div class="abs hdr" style="left:112px">Product</div>
<div class="abs hdr" style="left:234px">Supplier Part#</div>
<div class="abs hdr" style="left:354px">Open Qty</div>
<div class="abs hdr" style="left:467px">Unit</div>
<div class="abs hdr" style="left:583px">Unit Price</div>
<div class="abs hdr" style="left:696px">Extended</div>
<div class="abs hdr" style="left:784px">LI Type / Ship To</div>
<div class="check" style="left:991px;top:371px"></div>

<div class="abs txt link" style="left:38px;top:414px">10</div>
<div class="field" style="left:111px;top:408px;width:83px">P-1200</div>
<svg style="left:203px;top:413px" width="18" height="18" viewBox="0 0 18 18" fill="none" stroke="#3b82d6" stroke-width="2"><circle cx="7" cy="7" r="5.5"/><path d="M11 11l6 6"/></svg>
<div class="check" style="left:264px;top:411px"></div>
<div class="field" style="left:356px;top:408px;width:82px">1</div>
<div class="field sel" style="left:467px;top:408px;width:83px">EA</div>
<div class="field" style="left:583px;top:408px;width:83px">$6.50</div>
<div class="abs txt link" style="left:697px;top:411px;font-size:15px">$6.50</div>
<div class="field sel" style="left:784px;top:408px;width:180px">Receive&amp;Pay</div>
<div class="check" style="left:991px;top:411px"></div>
<div class="field" style="left:111px;top:443px;width:555px">Millbrook 389317- Brochure Paper, Ultra Smooth Text, 8 1/2" x 11", 28 lb., 96 Brightness</div>
<div class="abs txt" style="left:697px;top:446px;color:var(--blue);font-style:italic">ALCH</div>
<div class="field sel" style="left:784px;top:443px;width:180px"></div>
<div class="abs txt" style="left:136px;top:479px">On Purchase Orders <span class="link">30</span></div>
<div class="abs txt" style="left:356px;top:479px">Availiable <span style="color:var(--blue)">&nbsp;0</span></div>
<div class="abs txt" style="left:582px;top:479px;color:var(--red);text-decoration:underline">Over Budget</div>
<div class="abs txt" style="left:696px;top:479px;color:var(--red)">Pending</div>
<svg style="left:811px;top:478px" width="19" height="24" viewBox="0 0 19 24" fill="none" stroke="#3b82d6" stroke-width="1.3"><path d="M1 1h12l5 5v17H1zM4 9h11M4 12h11M4 15h11M4 18h11"/></svg>
<svg style="left:869px;top:478px" width="22" height="22" viewBox="0 0 22 22"><rect x="1" y="3" width="20" height="18" fill="none" stroke="#3b82d6" stroke-width="1.5"/><rect x="1" y="3" width="20" height="5" fill="#3b82d6"/><path d="M4 11h14M4 14h14M4 17h14M7 9v11M11 9v11M15 9v11" stroke="#3b82d6"/></svg>

<div class="abs band" style="top:507px;height:107px"></div>
<div class="abs txt link" style="left:38px;top:521px">20</div>
<div class="field" style="left:111px;top:515px;width:83px">P-1100</div>
<svg style="left:203px;top:520px" width="18" height="18" viewBox="0 0 18 18" fill="none" stroke="#3b82d6" stroke-width="2"><circle cx="7" cy="7" r="5.5"/><path d="M11 11l6 6"/></svg>
<div class="check" style="left:264px;top:518px"></div>
<div class="field" style="left:356px;top:515px;width:82px">1</div>
<div class="field sel" style="left:467px;top:515px;width:83px">EA</div>
<div class="field" style="left:583px;top:515px;width:83px">$5.00</div>
<div class="abs txt link" style="left:697px;top:518px;font-size:15px">$5.00</div>
<div class="field sel" style="left:784px;top:515px;width:180px">Receive&amp;Pay</div>
<div class="check" style="left:991px;top:518px"></div>
<div class="field" style="left:111px;top:550px;width:555px">Snowcrest 454230 - Recycled Laser Paper 1 case(2,500 count)- 24lb, 90 bright</div>
<div class="abs txt" style="left:697px;top:553px;color:var(--blue);font-style:italic">ALCH</div>
<div class="field sel" style="left:784px;top:550px;width:180px"></div>
<div class="abs txt" style="left:136px;top:586px">On Purchase Orders <span class="link">170</span></div>
<div class="abs txt" style="left:356px;top:586px">Availiable <span style="color:var(--blue)">&nbsp;0</span></div>
<div class="abs txt" style="left:582px;top:586px;color:var(--red);text-decoration:underline">Over Budget</div>
<div class="abs txt" style="left:696px;top:586px;color:var(--red)">Pending</div>
<svg style="left:811px;top:585px" width="19" height="24" viewBox="0 0 19 24" fill="none" stroke="#3b82d6" stroke-width="1.3"><path d="M1 1h12l5 5v17H1zM4 9h11M4 12h11M4 15h11M4 18h11"/></svg>
<svg style="left:869px;top:585px" width="22" height="22" viewBox="0 0 22 22"><rect x="1" y="3" width="20" height="18" fill="none" stroke="#3b82d6" stroke-width="1.5"/><rect x="1" y="3" width="20" height="5" fill="#3b82d6"/><path d="M4 11h14M4 14h14M4 17h14M7 9v11M11 9v11M15 9v11" stroke="#3b82d6"/></svg>

<div class="abs band" style="top:614px;height:181px"></div>
<div class="field" style="left:33px;top:622px;width:52px"></div>
<div class="field" style="left:111px;top:622px;width:83px"></div>
<svg style="left:203px;top:627px" width="18" height="18" viewBox="0 0 18 18" fill="none" stroke="#3b82d6" stroke-width="2"><circle cx="7" cy="7" r="5.5"/><path d="M11 11l6 6"/></svg>
<div class="check" style="left:264px;top:625px"></div>
<div class="field" style="left:356px;top:622px;width:82px"></div>
<div class="field sel" style="left:467px;top:622px;width:83px"></div>
<div class="field" style="left:583px;top:622px;width:83px"></div>
<div class="field sel" style="left:784px;top:622px;width:180px">Receive&amp;Pay</div>
<div class="field" style="left:111px;top:657px;width:555px"></div>
<div class="field sel" style="left:784px;top:657px;width:180px"></div>
<div class="field" style="left:913px;top:682px;width:34px;height:22px;border-top:none"></div>

<div class="abs bottombar">
  <svg style="left:17px;top:19px" width="28" height="28" viewBox="0 0 28 28" fill="none" stroke="#3b82d6" stroke-width="2"><path d="M22 12L12 22a5 5 0 01-7-7L16 4a3.5 3.5 0 015 5L10 20a2 2 0 01-3-3l9-9"/></svg>
  <svg style="left:61px;top:17px" width="28" height="30" viewBox="0 0 28 30" fill="none" stroke="#3b82d6" stroke-width="1.5"><path d="M17 27H2V2h13l5 5v6M5 9h11M5 13h8M5 17h6"/><circle cx="18" cy="20" r="4"/><path d="M21 23l4 4"/></svg>
  <svg style="left:103px;top:19px" width="28" height="28" viewBox="0 0 28 28" fill="#3b82d6"><circle cx="22" cy="5" r="4"/><circle cx="6" cy="14" r="4"/><circle cx="22" cy="23" r="4"/><path d="M22 5L6 14l16 9" stroke="#3b82d6" stroke-width="2" fill="none"/></svg>
  <svg style="left:155px;top:18px" width="32" height="30" viewBox="0 0 32 30" fill="none" stroke="#3b82d6" stroke-width="1.5"><rect x="1" y="7" width="30" height="21"/><path d="M11 7V2h10v5M1 16h30M8 13v6M24 13v6"/></svg>
  <svg style="left:209px;top:17px" width="32" height="32" viewBox="0 0 32 32" fill="none" stroke="#6b7280" stroke-width="1.6"><circle cx="16" cy="16" r="14"/><path d="M12 12a4 4 0 118 0c0 3-4 3-4 7"/><circle cx="16" cy="24" r="1" fill="#6b7280"/></svg>
  <svg style="left:261px;top:18px" width="30" height="30" viewBox="0 0 30 30" fill="none" stroke="#3b82d6" stroke-width="1.8"><path d="M3 27L18 12M8 3l19 19-4 4L4 7zM21 3a5 5 0 016 6l-3 3-6-6z"/></svg>
  <div class="t" style="left:298px">View GL Accounts</div>
  <svg style="left:458px;top:21px" width="36" height="28" viewBox="0 0 36 28"><rect x="1" y="1" width="28" height="20" fill="none" stroke="#3b82d6" stroke-width="2"/><rect x="1" y="1" width="28" height="6" fill="#3b82d6"/><rect x="5" y="11" width="10" height="3" fill="#3b82d6"/><circle cx="29" cy="21" r="6" fill="#4cb84c"/><path d="M29 18v6M26 21h6" stroke="#fff" stroke-width="1.6"/></svg>
  <div class="t" style="left:503px">Post Order</div>
  <div class="abs hint">Click Search, or enter property<br>values and click Apply</div>
  <svg style="left:968px;top:18px" width="30" height="30" viewBox="0 0 30 30" fill="none" stroke="#6b7280" stroke-width="2.6"><circle cx="12" cy="12" r="9"/><path d="M19 19l9 9"/></svg>
  <svg style="left:1011px;top:18px" width="30" height="30" viewBox="0 0 30 30" stroke="#6b7280" stroke-width="2.4"><path d="M15 1v28M1 15h28"/></svg>
  <svg style="left:1053px;top:16px" width="30" height="32" viewBox="0 0 30 32" fill="none" stroke="#3b82d6" stroke-width="3.2"><path d="M9 3L3 10l7 6M3 10h13a9 9 0 010 18h-2"/></svg>
  <svg style="left:1096px;top:20px" width="36" height="28" viewBox="0 0 36 28" fill="none" stroke="#4cb84c" stroke-width="4"><path d="M2 14l11 11L34 3"/></svg>
  <svg style="left:1150px;top:20px" width="28" height="28" viewBox="0 0 28 28" stroke="#e5455f" stroke-width="4"><path d="M2 2l24 24M26 2L2 26"/></svg>
</div>

</div>
</body>
</html>
```